Web site for Tree Removal Company

What we are looking for:
-------------------------------
Looking for a wordpress web site, you can provide your own template or we can supply you with one (http://quorvel.plindatheme.net).

What we do
---------------
To see what we do please go to google Australia and google "Tree removal Sydney" or "Tree Removal Melbourne".

Web site requirements
-----------------------------
We prefer you to use our template as it has all our requirements in already.
- Responsive.
- Based on Wordpress.
- Full complaint and compatible with plugs.

Look, Feel and Appearance
------------------------------------
Please use the logo (see attached), for colour scheme, look and feel of the web site.

Thank you for your time and effort!

Target Market(s)

Tree Removal for Residential Homes

Industry/Entity Type

It Company

Number of Pages Required

4 page

Font styles to use
Serif
Sans Serif

Requirements
Must have
• Wordpress
Nice to have
• Original artwork, images and text
Should not have
• non related images or wording

```html
<!DOCTYPE html>
<html lang="en">
<head>
<meta charset="utf-8">
<title>Bough &amp; Co — Tree Removal</title>
<link href="https://fonts.googleapis.com/css2?family=Raleway:wght@400;600;700&family=Open+Sans:wght@400;600&display=swap" rel="stylesheet">
<style>
:root{
  --bg:#0b0c0b;
  --panel:#222423;
  --green:#5c9f7c;
  --green-dark:#3f7a5b;
  --text:#e6e9e6;
  --muted:#a9aeaa;
  --line:#2f3330;
  --sky-top:#0f2a35;
  --sky-mid:#3f7f96;
  --grass:#3f7d2a;
}
*{box-sizing:border-box;margin:0;padding:0}
html,body{width:1200px;height:2740px;overflow:hidden;background:var(--bg)}
body{position:relative;font-family:"Open Sans",Arial,sans-serif;color:var(--text)}
.abs{position:absolute}

/* header / hero */
.hero{left:0;top:0;width:1200px;height:560px;
  background:linear-gradient(180deg,var(--sky-top) 0%,#2d6478 30%,var(--sky-mid) 52%,#6fa35a 66%,var(--grass) 78%,#1a2a14 92%,var(--bg) 100%)}
.nav-band{left:0;top:0;width:1200px;height:96px;background:linear-gradient(180deg,rgba(0,0,0,.75),rgba(0,0,0,.15))}
.nav{top:58px;display:flex;gap:30px;font-family:"Raleway",sans-serif;font-size:14px;font-weight:600;letter-spacing:.5px;color:#fff;text-transform:uppercase}
.nav-left{left:220px}
.nav-right{left:702px}
.nav a{color:inherit;text-decoration:none;padding-bottom:8px}
.nav a.active{border-bottom:2px solid var(--green)}
.brand-mark{left:564px;top:8px;width:72px;height:72px;border-radius:50%;background:var(--green-dark)}
.brand-name{left:500px;top:86px;width:200px;text-align:center;font-family:"Raleway",sans-serif;font-weight:700;font-size:16px;letter-spacing:3px;color:#fff;text-transform:uppercase}

/* feature cards */
.card{top:500px;width:276px;height:320px}
.card-photo{width:276px;height:188px}
.card-body{height:132px;background:var(--green);padding:34px 18px 0;text-align:center;position:relative}
.card-icon{position:absolute;left:110px;top:-28px;width:56px;height:56px;border-radius:50%;background:var(--green);border:3px solid #fff}
.card-title{font-family:"Raleway",sans-serif;font-size:13px;font-weight:700;color:#fff;text-transform:uppercase}
.card-text{margin-top:8px;font-size:12px;line-height:17px;color:#eef5f0}

/* sections */
.section-title{left:172px;font-family:"Raleway",sans-serif;font-weight:700;font-size:17px;color:#fff;text-transform:uppercase;letter-spacing:.3px}
.service-box{width:328px;background:var(--panel);padding:30px 26px}
.service-box h3{font-family:"Raleway",sans-serif;font-size:13px;font-weight:700;text-transform:uppercase;color:#fff;margin-bottom:14px}
.service-box p{font-size:12.5px;line-height:22px;color:var(--muted)}
.read-more{display:block;margin-top:34px;font-size:12px;color:#fff}

.photo-sydney{background:linear-gradient(160deg,#5a5a3c,#8b8a5a 40%,#3f4a2b 80%)}
.photo-melbourne{background:linear-gradient(200deg,#3c2f22,#7a6a4c 40%,#3e5a2a 85%)}
.g1{background:linear-gradient(150deg,#4f6a3a,#2c3b22)}
.g2{background:linear-gradient(150deg,#5a4a3c,#2a2a1e)}
.g3{background:linear-gradient(150deg,#3a3e36,#1e201c)}
.g4{background:linear-gradient(180deg,#6a7a8a,#c49a5a 55%,#2a2a1a)}
.g5{background:linear-gradient(180deg,#5c7290,#4a5a2c 70%,#24301a)}
.g6{background:linear-gradient(160deg,#7a4a2a,#3e5a2a 60%,#1e2a16)}
.c1{background:linear-gradient(180deg,#4f8fb4,#6aa8c4 60%,#5d8a3c)}
.c2{background:linear-gradient(180deg,#b88a4a,#d8b06a 60%,#6a5a2c)}
.c3{background:linear-gradient(180deg,#2c6a78,#3f8a7c 60%,#4a7a3a)}

/* footer */
.footer-art{left:0;top:2260px;width:1200px;height:480px;background:radial-gradient(ellipse 420px 300px at 600px 300px,#2a322c 0%,#151816 60%,var(--bg) 100%)}
.footer-head{font-family:"Raleway",sans-serif;font-weight:700;font-size:15px;text-transform:uppercase;color:#fff;top:2320px}
.list{top:2360px;list-style:none;font-size:12px;line-height:22px;color:var(--muted)}
.list li::before{content:"";display:inline-block;width:4px;height:4px;border-radius:50%;background:var(--green);margin:0 10px 2px 0;vertical-align:middle}
.subscribe-text{left:652px;top:2356px;width:380px;font-size:12px;line-height:18px;color:var(--muted)}
.field{height:40px;border:1px solid #6d736f;color:#cfd3d0;font-size:12px;padding:12px 14px;background:rgba(0,0,0,.3)}
.btn{left:896px;top:2480px;width:136px;height:40px;background:var(--green);color:#fff;font-size:12px;text-align:center;line-height:40px}
.rule{left:172px;top:2580px;width:860px;height:1px;background:var(--line)}
.socials{left:500px;top:2632px;display:flex;gap:12px}
.socials span{width:32px;height:32px;border-radius:50%;background:#e9ece9;display:block}
.copyright{left:0;top:2684px;width:1200px;text-align:center;font-size:11px;color:var(--muted)}
</style>
</head>
<body>

<header>
  <div class="abs hero" role="img" aria-label="Hero photograph of a large tree on rolling green hills under a blue sky"></div>
  <div class="abs nav-band"></div>
  <nav class="abs nav nav-left"><a class="active">Home</a><a>About Us</a><a>Blog</a></nav>
  <div class="abs brand-mark"></div>
  <div class="abs brand-name">Bough &amp; Co</div>
  <nav class="abs nav nav-right"><a>Products</a><a>Gallery</a><a>Contact Us</a></nav>
</header>

<section>
  <article class="abs card" style="left:172px">
    <div class="card-photo c1" role="img" aria-label="Photo of a single tree in a field"></div>
    <div class="card-body"><div class="card-icon"></div>
      <div class="card-title">Lorem ipsum dolor sit amet</div>
      <p class="card-text">Safe pruning and removal for residential gardens.</p></div>
  </article>
  <article class="abs card" style="left:462px">
    <div class="card-photo c2" role="img" aria-label="Photo of a spreading tree at golden hour"></div>
    <div class="card-body"><div class="card-icon"></div>
      <div class="card-title">Lorem ipsum dolor sit amet</div>
      <p class="card-text">Stump grinding and full site clean up.</p></div>
  </article>
  <article class="abs card" style="left:756px">
    <div class="card-photo c3" role="img" aria-label="Photo of a tree on a green hillside"></div>
    <div class="card-body"><div class="card-icon"></div>
      <div class="card-title">Lorem ipsum dolor sit amet</div>
      <p class="card-text">Health checks and advice from our arborists.</p></div>
  </article>
</section>

<section>
  <h2 class="abs section-title" style="top:876px">Tree Removal Sydney</h2>
  <div class="abs photo-sydney" style="left:172px;top:912px;width:516px;height:368px" role="img" aria-label="Photo of arborists clearing branches with a wood chipper"></div>
  <div class="abs service-box" style="left:704px;top:912px;height:356px">
    <h3>Lorem ipsum dolor sit amet</h3>
    <p>Our certified arborists remove unsafe and unwanted trees across Sydney with care. We assess every site, protect your garden and property, and clear away all timber and green waste. Fully insured crews, modern equipment and honest quotes for every residential job.</p>
    <span class="read-more">Read More</span>
  </div>
</section>

<section>
  <h2 class="abs section-title" style="top:1322px">Tree Removal Melbourne</h2>
  <div class="abs service-box" style="left:172px;top:1360px;height:352px">
    <h3>Lorem ipsum dolor sit amet</h3>
    <p>Our local team handles tree removal across Melbourne, from small backyard trees to large gums near homes. We work safely around roofs, fences and power lines, grind stumps on request and leave your yard clean. Free quotes and friendly advice.</p>
    <span class="read-more">Read More</span>
  </div>
  <div class="abs photo-melbourne" style="left:520px;top:1360px;width:512px;height:360px" role="img" aria-label="Photo of a worker in hi-vis cutting a large tree trunk"></div>
</section>

<section>
  <h2 class="abs section-title" style="top:1790px">Bough &amp; Co Gallery</h2>
  <div class="abs g1" style="left:172px;top:1828px;width:276px;height:204px" role="img" aria-label="Gallery photo of a tree spade digging"></div>
  <div class="abs g2" style="left:464px;top:1828px;width:276px;height:204px" role="img" aria-label="Gallery photo of twisted tree branches"></div>
  <div class="abs g3" style="left:756px;top:1828px;width:276px;height:204px" role="img" aria-label="Gallery photo of potted trees in a nursery"></div>
  <div class="abs g4" style="left:172px;top:2048px;width:276px;height:212px" role="img" aria-label="Gallery photo of a tree at sunset"></div>
  <div class="abs g5" style="left:464px;top:2048px;width:276px;height:212px" role="img" aria-label="Gallery photo of a lone tree in a meadow"></div>
  <div class="abs g6" style="left:756px;top:2048px;width:276px;height:212px" role="img" aria-label="Gallery photo of an autumn forest path"></div>
</section>

<footer>
  <div class="abs footer-art" role="img" aria-label="Faint silhouette of a large tree behind the footer"></div>
  <h2 class="abs footer-head" style="left:172px">Services</h2>
  <ul class="abs list" style="left:172px">
    <li>Tree Pruning</li><li>Shrub Pruning</li><li>Branch Cabling &amp; Canopy Support</li>
    <li>Tree Removal</li><li>Stump Grinding</li><li>Landscaping</li>
  </ul>
  <ul class="abs list" style="left:432px">
    <li>Soil &amp; Root Fertilisation</li><li>Insect &amp; Disease Control</li><li>Tree Collar Installation</li>
    <li>Winter Storm Protection</li><li>Managing Tree Defects</li><li>Tree Management Program</li>
  </ul>
  <h2 class="abs footer-head" style="left:652px">Subscribe</h2>
  <p class="abs subscribe-text">Subscribe to our newsletter. We won't spam you or sell your email.</p>
  <div class="abs field" style="left:652px;top:2420px;width:380px">First Name</div>
  <div class="abs field" style="left:652px;top:2480px;width:236px">Email</div>
  <div class="abs btn">Subscribe Now</div>
  <div class="abs rule"></div>
  <div class="abs socials"><span></span><span></span><span></span><span></span><span></span></div>
  <p class="abs copyright">Copyright © 2016 Bough &amp; Co | Privacy policy</p>
</footer>

</body>
</html>
```